Create a Graphic About YOURSELF and PixelHarbor

PixelHarbor would like you (designers) to create an awesome graphic to promote YOURSELF and your profile on PixelHarbor!

Your graphic should communicate your name, your services and should mention PixelHarbor.

The design should be perfect for sharing on Chatterly. Here's an example of what we'd like http://blog.pixelharbor-example.ca/article/333/pixelharbor-launches-3000-hire-me-social-design-contest

Once you submitted your design, we'd love you to share the design ('advertisement') and promote yourself and PixelHarbor to your friends and potential customers. So make your submissions great and get your friends to vote for your design by 'Liking' it on Chatterly!

Prizes:
$1500 - "PixelHarbor Community" prize awarded to the designer with the most Chatterly 'Likes'
5 x $50 for the next 5 'most liked' designs on Chatterly

$1000 - "Hire Me" prize awarded to the designer who receives the most client invites
5 x $50 for the next 5 'most invited' designers

In summary, this is a great opportunity for you to increase your exposure to PixelHarbor customers and win cash prizes. Show off your design skills and get hired by PixelHarbor customers from around the world!

Target Market(s)

Fans, friends and customers of YOU

Industry/Entity Type

Cash

Requirements
Must have
• 1) Include your PixelHarbor user name on the graphic so customers can find you in the PixelHarbor Designer Directory
2) Include the tagline "Hire Me on PixelHarbor.com!" in your graphic design.
3) Share your design's URL on our Chatterly wall at http://chatterly-example.com/pixelharbor and get your friends to 'like' your design.
Nice to have
• 1) Include a tagline that expresses your design approach/philosophy
2) Artwork dimensions: 403 x 403 px
3) You can submit more than 1 design!
Should not have
• You must own the copyright of any images you use including stock imagery.

```html
<!DOCTYPE html>
<html lang="en">
<head>
<meta charset="utf-8">
<title>Hire Me – Design &amp; Marketing</title>
<link rel="stylesheet" href="https://fonts.googleapis.com/css2?family=Bebas+Neue&family=Oswald:wght@600&display=swap">
<style>
  :root {
    --paper: #ffffff;
    --ink: #000000;
    --accent-blue: #1673bb;
    --pattern-grey: #d0d0d0;
    --url-grey: #a3a3a3;
  }
  html, body {
    margin: 0;
    padding: 0;
    width: 928px;
    height: 1200px;
    overflow: hidden;
    background: var(--paper);
  }
  .poster {
    display: block;
    width: 928px;
    height: 1200px;
  }
  .pattern-row {
    font-family: "Oswald", "Bebas Neue", sans-serif;
    font-weight: 600;
    font-size: 60px;
    fill: var(--pattern-grey);
  }
  .headline {
    font-family: "Bebas Neue", "Oswald", sans-serif;
    font-size: 752px;
  }
  .headline-hire { fill: var(--ink); }
  .headline-me { fill: var(--accent-blue); }
  .headline-bang { fill: var(--ink); }
  .site-url {
    font-family: "Bebas Neue", "Oswald", sans-serif;
    font-size: 112px;
    fill: var(--url-grey);
  }
</style>
</head>
<body>
<svg class="poster" viewBox="0 0 928 1200" xmlns="http://www.w3.org/2000/svg" aria-label="Hire Me! design.novaart.com">
  <g class="pattern" aria-hidden="true">
    <text class="pattern-row" x="-20" y="48">ESIGN &amp; MARKETING DESIGN &amp; MARKETING DESIGN</text>
    <text class="pattern-row" x="-20" y="102">ESIGN &amp; MARKETING DESIGN &amp; MARKETING DESIGN</text>
    <text class="pattern-row" x="-20" y="156">ESIGN &amp; MARKETING DESIGN &amp; MARKETING DESIGN</text>
    <text class="pattern-row" x="-20" y="210">ESIGN &amp; MARKETING DESIGN &amp; MARKETING DESIGN</text>
    <text class="pattern-row" x="-20" y="264">ESIGN &amp; MARKETING DESIGN &amp; MARKETING DESIGN</text>
    <text class="pattern-row" x="-20" y="318">ESIGN &amp; MARKETING DESIGN &amp; MARKETING DESIGN</text>
    <text class="pattern-row" x="-20" y="372">ESIGN &amp; MARKETING DESIGN &amp; MARKETING DESIGN</text>
    <text class="pattern-row" x="-20" y="426">ESIGN &amp; MARKETING DESIGN &amp; MARKETING DESIGN</text>
    <text class="pattern-row" x="-20" y="480">ESIGN &amp; MARKETING DESIGN &amp; MARKETING DESIGN</text>
    <text class="pattern-row" x="-20" y="534">ESIGN &amp; MARKETING DESIGN &amp; MARKETING DESIGN</text>
    <text class="pattern-row" x="-20" y="588">ESIGN &amp; MARKETING DESIGN &amp; MARKETING DESIGN</text>
    <text class="pattern-row" x="-20" y="642">ESIGN &amp; MARKETING DESIGN &amp; MARKETING DESIGN</text>
    <text class="pattern-row" x="-20" y="696">ESIGN &amp; MARKETING DESIGN &amp; MARKETING DESIGN</text>
    <text class="pattern-row" x="-20" y="750">ESIGN &amp; MARKETING DESIGN &amp; MARKETING DESIGN</text>
    <text class="pattern-row" x="-20" y="804">ESIGN &amp; MARKETING DESIGN &amp; MARKETING DESIGN</text>
    <text class="pattern-row" x="-20" y="858">ESIGN &amp; MARKETING DESIGN &amp; MARKETING DESIGN</text>
    <text class="pattern-row" x="-20" y="912">ESIGN &amp; MARKETING DESIGN &amp; MARKETING DESIGN</text>
    <text class="pattern-row" x="-20" y="966">ESIGN &amp; MARKETING DESIGN &amp; MARKETING DESIGN</text>
    <text class="pattern-row" x="-20" y="1020">ESIGN &amp; MARKETING DESIGN &amp; MARKETING DESIGN</text>
    <text class="pattern-row" x="-20" y="1074">ESIGN &amp; MARKETING DESIGN &amp; MARKETING DESIGN</text>
    <text class="pattern-row" x="-20" y="1128">ESIGN &amp; MARKETING DESIGN &amp; MARKETING DESIGN</text>
    <text class="pattern-row" x="-20" y="1182">ESIGN &amp; MARKETING DESIGN &amp; MARKETING DESIGN</text>
  </g>

  <text class="headline headline-hire" x="54" y="557" textLength="851" lengthAdjust="spacingAndGlyphs">HIRE</text>
  <text class="headline headline-me" x="54" y="1160" textLength="526" lengthAdjust="spacingAndGlyphs">ME</text>
  <text class="headline headline-bang" x="619" y="1160" textLength="70" lengthAdjust="spacingAndGlyphs">!</text>

  <g class="site">
    <text class="site-url" transform="translate(772 590) rotate(90)" textLength="258" lengthAdjust="spacingAndGlyphs">DESIGN.</text>
    <text class="site-url" x="727" y="936" textLength="131" lengthAdjust="spacingAndGlyphs">NOVA</text>
    <text class="site-url" x="740" y="1030" textLength="110" lengthAdjust="spacingAndGlyphs">ART</text>
    <text class="site-url" x="727" y="1153" textLength="158" lengthAdjust="spacingAndGlyphs">.COM</text>
  </g>
</svg>
</body>
</html>
```